An hotel welcome folder kit
luxury suites in NYC
An hotel  welcome folder kit -
Creative Brief
We are looking for to set up a beautiful welcome folder for our suites guests. This folder will be placed in the room on the bed. Within this folder they will find the whole info they need in order to get around the building they are staying in,about our services, the location. amenities, attractions etc. here is some info about what our business about: Morvane Lodgings offers various luxury vacation suites in beautiful luxury residential buildings around Manhattan and are rented out to tourists on a short term basis a la a hotel. The suites and buildings come fully equipped with all the necessary amenities and more: - wireless internet & high definition television with digital cable in unit - On site laundry room - Fantastic fully equipped gym - Residential lounge area with billiards table - Amazing roof deck with breathtaking views of the city.
our suites guests.
The welcome kit is a folder that has a one pocket on the right hand side of the folder inside. in this pocket we will place the pages with the info the guests need to know. on the left hand side inside the folder we will pitch our hotel concept (1-2 short sentences). on the cover of the folder we would like to see our logo and the name of the hotel the logo file is attached. what do we need from you: 1.a design of the folder based on our logo (colors ans font) : cover , left hand side inside the folder, on the back of the folder our contact info 2. a design of a template for the pages that we will place inside the folder (each page has its own topic for example: one page is about our services, the second page is info about attractions in the city..etc) important: the design should present out consept of luxury , high end style, Cutting-Edge Unique/Creative,Clean/Simple, Sophisticated. info about the logo: Brown #CFBA76 R:207 G:186 B:118 Font:Rage Italic Font2: Arial tagline: Arial dark Gray: #333333 R:51 G:51 B:51 Thanks a lot!!!

```html
<!DOCTYPE html>
<html lang="en">
<head>
<meta charset="utf-8">
<title>Morvane Lodgings – Welcome Folder</title>
<link rel="stylesheet" href="https://fonts.googleapis.com/css2?family=Great+Vibes&family=Arimo:wght@400;700&display=swap">
<style>
  :root{
    --gold:#cfba76;
    --gold-deep:#a88f4c;
    --cream:#f3ead6;
    --sand:#d9c7a0;
    --charcoal:#333333;
    --black:#0d0b09;
    --paper:#ffffff;
    --text:#4a4a4a;
  }
  *{margin:0;padding:0;box-sizing:border-box}
  html,body{width:1200px;height:406px;overflow:hidden;background:var(--paper)}
  body{position:relative;font-family:"Arimo",Arial,sans-serif;color:var(--text)}
  .spread{position:absolute;top:10px;height:386px;overflow:hidden;box-shadow:0 0 4px rgba(0,0,0,.25)}
  .spread--outside{left:10px;width:578px;background:var(--black)}
  .spread--inside{left:612px;width:578px;background:var(--paper)}
  .block{position:absolute}
  .photo{position:absolute}
  .script{font-family:"Great Vibes",cursive;font-weight:400;color:var(--gold)}
  .brand{position:absolute;display:flex;align-items:center;gap:6px}
  .brand__dot{width:8px;height:8px;border-radius:50%;background:var(--gold)}
  .brand__name{font-family:"Great Vibes",cursive;color:var(--gold);line-height:1}
  .small{font-size:5.5px;line-height:1.45;color:#d8d0bd}
  .body-copy{position:absolute;font-size:5.6px;line-height:1.5;color:var(--text)}
  .body-copy p+p{margin-top:5px}
  .body-copy ul{list-style:none;margin-top:4px}
  .body-copy li::before{content:"";display:inline-block;width:3px;height:3px;background:var(--gold);border-radius:50%;margin-right:4px;vertical-align:middle}
</style>
</head>
<body>

<!-- Outside of the folder: back panel + front cover -->
<section class="spread spread--outside">
  <!-- back panel -->
  <div class="photo" role="img" aria-label="Photo of a hotel hallway with staircase, wooden cabinet and a leather suitcase"
       style="left:0;top:0;width:289px;height:300px;background:linear-gradient(160deg,#f1e6cf 0%,#d8c39a 45%,#8a6a43 100%)"></div>
  <svg class="block" style="left:0;top:240px" width="289" height="146" viewBox="0 0 289 146">
    <path d="M0 60 C70 30 140 90 210 60 C245 45 270 35 289 40 L289 146 L0 146Z" fill="var(--cream)"/>
    <path d="M0 78 C70 48 140 108 210 78 C245 63 270 53 289 58 L289 146 L0 146Z" fill="var(--black)"/>
  </svg>
  <div class="brand" style="left:16px;top:330px">
    <span class="brand__name" style="font-size:17px">Morvane Lodgings</span>
  </div>
  <div class="block small" style="left:16px;top:352px">
    123 Park Avenue, New York, NY 10016<br>
    Tel: 212 555 0148<br>
    stay@morvanelodgings.com<br>
    www.morvanelodgings.com
  </div>

  <!-- front cover -->
  <div class="block" style="left:289px;top:0;width:289px;height:386px;background:linear-gradient(180deg,#f4ebd7 0%,#e5d3ac 60%,#c9ad78 100%)"></div>
  <div class="photo" role="img" aria-label="Ornamental flourish pattern on the cover background"
       style="left:289px;top:0;width:70px;height:260px;background:linear-gradient(90deg,rgba(160,125,75,.45),rgba(160,125,75,0))"></div>
  <div class="photo" role="img" aria-label="Ornamental flourish pattern on the cover background"
       style="left:508px;top:0;width:70px;height:260px;background:linear-gradient(270deg,rgba(160,125,75,.45),rgba(160,125,75,0))"></div>
  <h1 class="block script" style="left:289px;width:289px;top:14px;text-align:center;font-size:38px;color:var(--gold-deep)">Welcome</h1>
  <p class="block" style="left:289px;width:289px;top:62px;text-align:center;font-size:6.5px;letter-spacing:1.2px;color:var(--charcoal);font-weight:700">A WONDERFUL RESTFUL STAY</p>
  <div class="photo" role="img" aria-label="Photo of a guest in a suit standing in a bright arched doorway, seen from behind"
       style="left:370px;top:84px;width:128px;height:200px;border-radius:64px 64px 0 0;background:linear-gradient(180deg,#fbf7ee 0%,#e8dcc2 55%,#b79a6a 100%)"></div>
  <svg class="block" style="left:289px;top:230px" width="289" height="156" viewBox="0 0 289 156">
    <path d="M0 40 C60 70 110 20 170 40 C220 58 255 50 289 30 L289 156 L0 156Z" fill="var(--gold)"/>
    <path d="M0 56 C60 86 110 36 170 56 C220 74 255 66 289 46 L289 156 L0 156Z" fill="var(--cream)"/>
    <path d="M0 66 C60 96 110 46 170 66 C220 84 255 76 289 56 L289 156 L0 156Z" fill="var(--black)"/>
  </svg>
  <div class="brand" style="left:289px;width:289px;top:322px;flex-direction:column;gap:4px">
    <span class="brand__dot"></span>
    <span class="brand__name" style="font-size:22px">Morvane Lodgings</span>
    <span class="small" style="color:var(--gold);letter-spacing:.6px">luxury suites in NYC</span>
  </div>
</section>

<!-- Inside of the folder -->
<section class="spread spread--inside">
  <!-- top strip -->
  <div class="photo" role="img" aria-label="Photo of a luxury suite bedroom with a made bed and lamps"
       style="left:0;top:0;width:150px;height:100px;background:linear-gradient(135deg,#e9dcc0 0%,#b59668 60%,#6e5232 100%)"></div>
  <div class="block" style="left:150px;top:0;width:368px;height:100px;background:linear-gradient(180deg,#f6eedc,#e7d6b0)"></div>
  <h2 class="block script" style="left:160px;top:4px;font-size:36px;color:var(--gold-deep)">Suites</h2>
  <h2 class="block script" style="left:340px;top:4px;font-size:36px;color:var(--gold-deep)">Facilities</h2>
  <p class="body-copy" style="left:160px;top:52px;width:160px">If you are dreaming of rest, relaxation and tranquility in a stunning setting with fully equipped suites, then we welcome you right here.</p>
  <p class="body-copy" style="left:340px;top:52px;width:170px">Morvane Lodgings offers fully equipped residential buildings around Manhattan rented to tourists on a short term basis.</p>
  <div class="photo" role="img" aria-label="Photo of a guest with luggage arriving at a hotel door"
       style="left:518px;top:0;width:60px;height:100px;background:linear-gradient(180deg,#d9c7a0 0%,#7e5f3a 100%)"></div>

  <!-- middle content -->
  <div class="body-copy" style="left:10px;top:112px;width:140px">
    <p>Each suite is furnished with care and designed for comfort, with generous living space, soft linens and quiet rooms above the city streets.</p>
    <p>Our team is here to help you plan your days, book tables and tours, and make every hour of your stay easy.</p>
  </div>
  <div class="photo" role="img" aria-label="Photo of guests relaxing in a residential lounge"
       style="left:158px;top:110px;width:120px;height:120px;background:linear-gradient(135deg,#eadfca 0%,#9c8060 100%)"></div>
  <div class="photo" role="img" aria-label="Photo of a rooftop pool deck with city views"
       style="left:284px;top:110px;width:100px;height:120px;background:linear-gradient(180deg,#9fc4dc 0%,#5f95b8 60%,#d9c7a0 100%)"></div>
  <div class="body-copy" style="left:394px;top:112px;width:176px">
    <p>Wireless internet and high definition television with digital cable in every unit.</p>
    <ul>
      <li>On site laundry room</li>
      <li>Fully equipped gym</li>
      <li>Lounge with billiards table</li>
      <li>Roof deck with city views</li>
    </ul>
    <p>Ask at the front desk for anything you need during your stay.</p>
  </div>

  <!-- bottom band -->
  <svg class="block" style="left:0;top:250px" width="578" height="136" viewBox="0 0 578 136">
    <path d="M0 20 C150 40 420 0 578 22 L578 136 L0 136Z" fill="var(--black)"/>
    <path d="M0 20 C150 40 420 0 578 22" fill="none" stroke="var(--gold)" stroke-width="1.5"/>
  </svg>
  <div class="brand" style="left:0;width:578px;top:318px;justify-content:center">
    <span class="brand__name" style="font-size:30px">Morvane Lodgings</span>
  </div>
</section>

</body>
</html>
```